VORN - Business cards

Business card to be created for Commercial sales staff

Target Market(s)

Commercial businesses

Industry/Entity Type

Commercial

Contact Information for Business Card

Look professional. For commercial clients

Colors
ffffff

Requirements
Must have
• - Vorn Logo
• - Commercial sales staff as postion
• - room for commerical sales manager role
• - person name and their mobile number
• - Website : vornelectrical.com.au
Nice to have
• White background.
• On back of business card just have the logo no other information
Should not have
• Should only have white background on front of card.

```html
<!DOCTYPE html>
<html lang="en">
<head>
<meta charset="utf-8">
<title>VORN – Business Cards</title>
<link href="https://fonts.googleapis.com/css2?family=Open+Sans:wght@400;600;700;800&display=swap" rel="stylesheet">
<style>
  :root {
    --page-bg: #e9e6e1;
    --card-white: #ffffff;
    --brand-red: #c40c14;
    --brand-charcoal: #33363d;
    --text-body: #3b3b3b;
  }
  * { margin: 0; padding: 0; box-sizing: border-box; }
  html, body {
    width: 1200px; height: 987px; overflow: hidden;
    background: var(--page-bg);
    font-family: "Open Sans", Arial, sans-serif;
  }
  .stage { position: relative; width: 1200px; height: 987px; }
  .card {
    position: absolute; left: 293px; width: 615px; height: 352px;
    box-shadow: 0 2px 6px rgba(0,0,0,0.25);
    overflow: hidden;
  }
  .card-front { top: 130px; background: var(--card-white); }
  .card-back { top: 506px; background: var(--brand-red); }

  .brand {
    position: absolute; display: flex; align-items: center; gap: 14px;
    font-weight: 800; letter-spacing: 2px; line-height: 1;
  }
  .brand-mark { width: 40px; height: 40px; border-radius: 50%; }
  .card-front .brand { right: 38px; top: 44px; font-size: 66px; color: var(--brand-charcoal); }
  .card-front .brand-mark { background: var(--brand-red); }
  .card-back .brand {
    left: 50%; top: 50%; transform: translate(-50%, -50%);
    font-size: 72px; color: var(--card-white);
  }
  .card-back .brand-mark { background: var(--card-white); }

  .holder { position: absolute; left: 39px; top: 167px; }
  .holder-name { font-size: 21px; font-weight: 600; color: var(--brand-red); letter-spacing: 0.3px; line-height: 1.1; }
  .holder-role { font-size: 16px; color: var(--text-body); margin-top: 4px; }
  .contact-list { list-style: none; margin-top: 14px; }
  .contact-list li {
    display: flex; align-items: center; gap: 7px;
    font-size: 15px; color: var(--text-body); line-height: 24px;
  }
  .contact-list svg { width: 14px; height: 14px; fill: var(--brand-red); flex: none; }

  .footer-band { position: absolute; left: 0; bottom: 0; width: 615px; height: 50px; }
  .website {
    position: absolute; right: 30px; bottom: 12px;
    font-size: 16px; color: var(--card-white);
  }
</style>
</head>
<body>
<main class="stage">
  <section class="card card-front" aria-label="Business card front">
    <div class="brand"><span class="brand-mark"></span>VORN</div>

    <div class="holder">
      <p class="holder-name">DAREN TOLLIVER</p>
      <p class="holder-role">Manager, Commerical Sales</p>
      <ul class="contact-list">
        <li>
          <svg viewBox="0 0 24 24" aria-hidden="true"><path d="M6.6 10.8a15.1 15.1 0 0 0 6.6 6.6l2.2-2.2c.3-.3.7-.4 1-.2 1.1.4 2.3.6 3.6.6.6 0 1 .4 1 1V20c0 .6-.4 1-1 1A17 17 0 0 1 3 4c0-.6.4-1 1-1h3.5c.6 0 1 .4 1 1 0 1.3.2 2.5.6 3.6.1.3 0 .7-.2 1z"/></svg>
          614 220 7391
        </li>
        <li>
          <svg viewBox="0 0 24 24" aria-hidden="true"><path d="M7 1h10a2 2 0 0 1 2 2v18a2 2 0 0 1-2 2H7a2 2 0 0 1-2-2V3a2 2 0 0 1 2-2zm0 3v14h10V4zm5 15.5a1 1 0 1 0 0 2 1 1 0 0 0 0-2z"/></svg>
          318 506 2294
        </li>
        <li>
          <svg viewBox="0 0 24 24" aria-hidden="true"><path d="M2 5h20v14H2zm2 2v.4l8 5.2 8-5.2V7zm0 2.8V17h16V9.8l-8 5.2z"/></svg>
          Daren@vornelectrical.com.au
        </li>
      </ul>
    </div>

    <svg class="footer-band" viewBox="0 0 615 50" aria-hidden="true">
      <rect x="0" y="26" width="360" height="8" fill="var(--brand-charcoal)"/>
      <rect x="0" y="38" width="615" height="12" fill="var(--brand-red)"/>
      <path d="M326 40 C341 40 344 7 368 7" fill="none" stroke="var(--card-white)" stroke-width="5"/>
      <path d="M330 40 C345 40 348 9 372 9 L615 9 L615 50 L330 50 Z" fill="var(--brand-red)"/>
    </svg>
    <p class="website">www.vornelectrical.com.au</p>
  </section>

  <section class="card card-back" aria-label="Business card back">
    <div class="brand"><span class="brand-mark"></span>VORN</div>
  </section>
</main>
</body>
</html>
```